Childcare Centre Franchise Website Design

Our business is Childcare centre, and we are the franchise with 4 centres currently, we would like to have the website similar as the link below,
https://www.brambleoak.edu.au/
with the same items, functions and pages. Locations information for all centres, and have pages for each centre. Additionally, we will need a page for online enrolment.
Our logo is attached.

```html
<!DOCTYPE html>
<html lang="en">
<head>
<meta charset="utf-8">
<title>Tiny Meadow Childcare</title>
<link href="https://fonts.googleapis.com/css2?family=Libre+Baskerville:wght@400;700&family=Lato:wght@400;700&display=swap" rel="stylesheet">
<style>
:root{
  --teal:#17a09b;
  --teal-dark:#128783;
  --pink:#d6426f;
  --pink-soft:#e3557f;
  --orange:#f26a38;
  --green:#8fc93a;
  --yellow:#f5c016;
  --ink:#1d1d1d;
  --text:#444;
  --grey-bg:#ececeb;
  --white:#fff;
}
*{margin:0;padding:0;box-sizing:border-box}
html,body{width:1200px;height:4047px;overflow:hidden}
body{position:relative;background:var(--white);font-family:"Lato",sans-serif;color:var(--text)}
.abs{position:absolute}

/* header */
.topbar{left:0;top:0;width:1200px;height:6px;background:var(--teal)}
.utility{left:400px;top:0;width:621px;height:52px;background:var(--teal);border-radius:0 0 22px 22px;display:flex;align-items:center;gap:36px;padding:0 40px;color:#fff;font-size:15px}
.utility .search{display:flex;align-items:center;gap:8px;border-bottom:1px solid #fff;width:160px;padding-bottom:4px}
.utility .phone{display:flex;align-items:center;gap:8px}
.utility .find{border:2px solid #fff;border-radius:20px;padding:5px 18px;font-family:"Libre Baskerville",serif;font-weight:700;font-size:13px;display:flex;gap:8px;align-items:center;margin-left:10px}
.brand{left:116px;top:76px;display:flex;align-items:center;gap:8px;font-family:"Libre Baskerville",serif;font-weight:700;color:var(--pink);font-size:19px}
.brand .dot{width:18px;height:18px;border-radius:50%;background:var(--green)}
.nav{left:322px;top:86px;font-size:13.5px;color:var(--ink)}
.nav span{position:absolute;white-space:nowrap}

/* hero */
.hero-photo{left:0;top:130px;width:605px;height:643px;background:linear-gradient(135deg,#d9a25a,#c9382f 35%,#3c6cc2 60%,#7c3f9f 85%,#e2c24c)}
.hero-panel{left:605px;top:130px;width:595px;height:643px;background:linear-gradient(140deg,#e0507a,#cf3a67)}
.hero-title{left:633px;top:268px;font-family:"Libre Baskerville",serif;font-weight:700;color:#fff;font-size:55px;line-height:64px;letter-spacing:1px}
.hero-text{left:636px;top:472px;width:500px;color:#fff;font-size:15px;line-height:25px}
.btn-start{left:633px;top:542px;width:160px;height:55px;background:#fff;border-radius:28px;color:var(--pink);font-family:"Libre Baskerville",serif;font-weight:700;font-size:13px;display:flex;align-items:center;justify-content:center}

/* section titles */
.sec-title{left:0;width:1200px;text-align:center;font-family:"Libre Baskerville",serif;font-weight:700;color:var(--ink);font-size:35px}

/* support cards */
.card{background:#fff;border-radius:20px;box-shadow:0 6px 28px rgba(0,0,0,.08);text-align:center}
.card h3{font-family:"Libre Baskerville",serif;font-weight:700;color:var(--ink);font-size:21px;line-height:30px}
.card p{font-size:14px;line-height:26px;color:#333}
.icon-circle{position:absolute;width:104px;height:104px;border-radius:50%;left:50%;margin-left:-52px;top:-26px;display:flex;align-items:center;justify-content:center}
.card.featured{border:2px solid var(--orange)}
.btn-learn{left:527px;top:1194px;width:148px;height:55px;border-radius:28px;background:var(--orange);color:#fff;font-weight:700;font-size:15px;display:flex;align-items:center;justify-content:center}

/* enrollment */
.enroll-bg{left:0;top:1332px;width:1200px;height:522px;background:var(--grey-bg)}
.enroll-text{left:175px;top:1446px;width:850px;text-align:center;font-size:15px;line-height:26px;color:#333}
.video-frame{left:155px;top:1587px;width:890px;height:484px;border:8px solid var(--pink);background:#fff}
.video{width:100%;height:100%;background:linear-gradient(160deg,#b8b0a4,#8e8477 50%,#cfc6bb);position:relative;border:2px solid #fff}
.play{position:absolute;left:50%;top:50%;width:50px;height:50px;margin:-25px 0 0 -25px;border-radius:50%;background:var(--orange);display:flex;align-items:center;justify-content:center}

/* states */
.states-bg{left:0;top:2176px;width:1200px;height:536px;background:linear-gradient(180deg,#1aa39e,#14938e)}
.state{top:2330px;width:231px;height:306px;border-radius:12px;overflow:hidden;color:#fff}
.state .img{position:absolute;inset:0}
.state .shade{position:absolute;left:0;right:0;bottom:0;height:170px;background:linear-gradient(180deg,rgba(0,0,0,0),rgba(0,0,0,.65))}
.state h4{position:absolute;left:17px;top:175px;font-family:"Libre Baskerville",serif;font-weight:700;font-size:16px}
.state p{position:absolute;left:17px;top:201px;width:200px;font-size:12px;line-height:21px}
.state .pill{position:absolute;left:17px;top:250px;width:112px;height:35px;border-radius:18px;font-family:"Libre Baskerville",serif;font-size:11px;display:flex;align-items:center;justify-content:center}

/* faq */
.faq-bg{left:0;top:2712px;width:1200px;height:736px;background:var(--grey-bg)}
.faq-item{left:196px;width:806px;height:72px;background:#fff;border-radius:36px;display:flex;align-items:center;padding:0 8px}
.faq-num{width:56px;height:56px;border-radius:50%;background:var(--green);color:#fff;font-family:"Libre Baskerville",serif;font-size:21px;display:flex;align-items:center;justify-content:center}
.faq-q{flex:1;margin-left:24px;font-family:"Libre Baskerville",serif;font-size:19px;color:var(--ink)}
.faq-toggle{width:30px;margin-right:26px;color:var(--green);font-size:28px;text-align:center;line-height:1}
.faq-item.open .faq-num{background:var(--orange)}
.faq-item.open .faq-toggle{color:var(--orange)}
.faq-answer{left:294px;top:3272px;width:660px;border-left:2px solid var(--orange);padding-left:16px;font-size:14.5px;line-height:26px;color:#333}
.faq-answer a{color:var(--orange)}

/* newsletter */
.news-input{left:198px;top:3594px;width:603px;height:56px;border:1px solid #666;border-right:none;display:flex;align-items:center;padding-left:26px;font-size:15px;color:#333}
.news-btn{left:801px;top:3594px;width:225px;height:56px;background:var(--pink);color:#fff;font-family:"Libre Baskerville",serif;font-weight:700;font-size:16px;display:flex;align-items:center;justify-content:center}
.foot-nav{top:3694px;font-size:13.5px;color:var(--ink);white-space:nowrap}
.rule{left:112px;width:976px;height:1px;background:#cfcfcf}
.foot-brand{left:124px;top:3862px;display:flex;align-items:center;gap:8px;font-family:"Libre Baskerville",serif;font-weight:700;color:var(--pink);font-size:20px}
.foot-brand .dot{width:20px;height:20px;border-radius:50%;background:var(--green)}
.contact-icon{width:46px;height:46px;border-radius:50%;display:flex;align-items:center;justify-content:center}
.contact{font-size:15px;line-height:26px;color:#333}
.contact b{font-family:"Libre Baskerville",serif;color:var(--ink);font-size:16px}
.copyright{left:0;top:3987px;width:1200px;text-align:center;font-size:14.5px;color:#333}
</style>
</head>
<body>

<header>
  <div class="abs topbar"></div>
  <div class="abs utility">
    <div class="search"><svg width="14" height="14" viewBox="0 0 14 14"><circle cx="6" cy="6" r="4.5" fill="none" stroke="#fff" stroke-width="2"/><line x1="9.5" y1="9.5" x2="13" y2="13" stroke="#fff" stroke-width="2"/></svg>Search</div>
    <div class="phone"><svg width="14" height="14" viewBox="0 0 24 24"><path fill="#fff" d="M6.6 10.8a15 15 0 0 0 6.6 6.6l2.2-2.2c.3-.3.7-.4 1-.2 1.1.4 2.3.6 3.6.6.6 0 1 .4 1 1V20c0 .6-.4 1-1 1A17 17 0 0 1 3 4c0-.6.4-1 1-1h3.5c.6 0 1 .4 1 1 0 1.3.2 2.5.6 3.6.1.3 0 .7-.2 1z"/></svg>1300 000 482</div>
    <div class="find"><svg width="10" height="14" viewBox="0 0 10 14"><path fill="#fff" d="M5 0a5 5 0 0 0-5 5c0 3.5 5 9 5 9s5-5.5 5-9a5 5 0 0 0-5-5zm0 7a2 2 0 1 1 0-4 2 2 0 0 1 0 4z"/></svg>Find a Centre</div>
  </div>
  <div class="abs brand"><span class="dot"></span>Tiny Meadow</div>
  <nav class="abs nav">
    <span style="left:0">Childcare &amp; Education</span>
    <span style="left:181px">ChildcareCentres</span>
    <span style="left:333px">Online Enrollment</span>
    <span style="left:485px">News &amp; Advice</span>
    <span style="left:622px">Careers</span>
    <span style="left:715px">About Us</span>
  </nav>
</header>

<section class="hero">
  <div class="abs hero-photo" role="img" aria-label="Children in colourful clothes lying in a circle on a play parachute, seen from above"></div>
  <div class="abs hero-panel"></div>
  <h1 class="abs hero-title">WELCOME TO<br>TINY MEADOW<br>CHILDCARE</h1>
  <p class="abs hero-text">Lorem ipsum dolor sit amet, consectetur adipiscing elit, sed do eiusmod tempor incididunt ut labore et dolore magna aliqua.</p>
  <div class="abs btn-start">GET STARTED</div>
</section>

<section class="support">
  <h2 class="abs sec-title" style="top:848px">We’re here to Support the Whole Family</h2>
  <div class="abs card" style="left:112px;top:952px;width:304px;height:223px">
    <div class="icon-circle" style="background:var(--pink)"><svg width="50" height="50" viewBox="0 0 50 50" fill="none" stroke="#fff" stroke-width="2"><path d="M12 30c4 6 10 10 18 8l8-3M18 22l8-8 3 3-6 7M24 26l9-10 3 3-8 9M14 28l-2-10 4-1 3 7"/><path d="M30 10c2-3 6-2 6 1 0 3-6 6-6 6s-6-3-6-6c0-3 4-4 6-1z"/></svg></div>
    <h3 style="margin-top:104px">Child Care Subsidy</h3>
    <p style="margin-top:10px">Lorem ipsum dolor sit amet,<br>consectetur adipiscing elit, sed do</p>
  </div>
  <div class="abs card featured" style="left:448px;top:952px;width:304px;height:270px">
    <div class="icon-circle" style="background:var(--orange)"><svg width="52" height="52" viewBox="0 0 52 52" fill="none" stroke="#fff" stroke-width="2"><circle cx="26" cy="16" r="5"/><circle cx="15" cy="24" r="4"/><circle cx="37" cy="24" r="4"/><path d="M17 42v-8c0-5 4-9 9-9s9 4 9 9v8M8 42v-6c0-4 3-6 7-6M44 42v-6c0-4-3-6-7-6"/></svg></div>
    <h3 style="margin-top:100px">Why Tiny Meadow<br>Childcare</h3>
    <p style="margin-top:14px">Lorem ipsum dolor sit amet,<br>consectetur adipiscing elit, sed do</p>
  </div>
  <div class="abs btn-learn">Learn More</div>
  <div class="abs card" style="left:782px;top:952px;width:305px;height:223px">
    <div class="icon-circle" style="background:var(--teal)"><svg width="50" height="50" viewBox="0 0 50 50" fill="none" stroke="#fff" stroke-width="2"><path d="M25 36s-10-6-10-13c0-4 5-6 10-1 5-5 10-3 10 1 0 7-10 13-10 13z"/><circle cx="10" cy="14" r="4"/><circle cx="40" cy="14" r="4"/><path d="M4 30c2-6 6-8 10-6M46 30c-2-6-6-8-10-6"/></svg></div>
    <h3 style="margin-top:104px">Health &amp; Wellbeing</h3>
    <p style="margin-top:10px">Lorem ipsum dolor sit amet,<br>consectetur adipiscing elit, sed do</p>
  </div>
</section>

<section class="enrollment">
  <div class="abs enroll-bg"></div>
  <h2 class="abs sec-title" style="top:1388px">Online Enrollment</h2>
  <p class="abs enroll-text">Lorem ipsum dolor sit amet, consectetur adipiscing elit, sed do eiusmod tempor incididunt ut labore et dolore magna aliqua. Quis ipsum suspendisse ultrices gravida. Risus commodo viverra maecenas accumsan lacus vel facilisis. Lorem ipsum dolor sit amet, consectetur adipiscing elit, sed do eiusmod tempor incididunt ut labore et dolore magna aliqua. Quis ipsum suspendisse ultrices gravida. Risus commodo viverra maecenas accumsan lacus vel facilisis.</p>
  <div class="abs video-frame">
    <div class="video" role="img" aria-label="Video still of two toddlers playing with soft toys and wooden blocks on a playroom floor">
      <div class="play"><svg width="14" height="16" viewBox="0 0 14 16"><path d="M2 1l11 7-11 7z" fill="#fff"/></svg></div>
    </div>
  </div>
</section>

<section class="states">
  <div class="abs states-bg"></div>
  <h2 class="abs sec-title" style="top:2240px;color:#fff">Childcare Centres by State</h2>
  <div class="abs state" style="left:112px">
    <div class="img" role="img" aria-label="Melbourne city skyline" style="background:linear-gradient(180deg,#7f9fbf,#9aa6ad 45%,#4d5358)"></div>
    <div class="shade"></div><h4>Victoria</h4>
    <p>Lorem ipsum dolor sit amet, consectetur adipiscing elit</p>
    <div class="pill" style="background:var(--orange)">Learn More</div>
  </div>
  <div class="abs state" style="left:360px">
    <div class="img" role="img" aria-label="Sydney harbour skyline" style="background:linear-gradient(180deg,#8aa3b8,#7d8a92 45%,#3f4a50)"></div>
    <div class="shade"></div><h4>New South Wales</h4>
    <p>Lorem ipsum dolor sit amet, consectetur adipiscing elit</p>
    <div class="pill" style="background:var(--green)">Learn More</div>
  </div>
  <div class="abs state" style="left:608px">
    <div class="img" role="img" aria-label="Brisbane city and river at sunset" style="background:linear-gradient(180deg,#6f8fb5,#c7a98a 45%,#4d4a47)"></div>
    <div class="shade"></div><h4>Queensland</h4>
    <p>Lorem ipsum dolor sit amet, consectetur adipiscing elit</p>
    <div class="pill" style="background:var(--yellow);color:#333">Learn More</div>
  </div>
  <div class="abs state" style="left:856px">
    <div class="img" role="img" aria-label="City skyline behind a steel arch bridge" style="background:linear-gradient(180deg,#7e9cc0,#b49c8a 45%,#4a4542)"></div>
    <div class="shade"></div><h4>South Australia</h4>
    <p>Lorem ipsum dolor sit amet, consectetur adipiscing elit</p>
    <div class="pill" style="background:var(--pink-soft)">Learn More</div>
  </div>
</section>

<section class="faq">
  <div class="abs faq-bg"></div>
  <h2 class="abs sec-title" style="top:2792px">Frequently Asked Questions</h2>
  <div class="abs faq-item" style="top:2881px"><div class="faq-num">01</div><div class="faq-q">Lorem ipsum dolor sit amet, consectetur adipiscing elit</div><div class="faq-toggle">+</div></div>
  <div class="abs faq-item" style="top:2980px"><div class="faq-num">02</div><div class="faq-q">Lorem ipsum dolor sit amet, consectetur adipiscing elit</div><div class="faq-toggle">+</div></div>
  <div class="abs faq-item" style="top:3082px"><div class="faq-num">03</div><div class="faq-q">Lorem ipsum dolor sit amet, consectetur adipiscing elit</div><div class="faq-toggle">+</div></div>
  <div class="abs faq-item open" style="top:3186px"><div class="faq-num">04</div><div class="faq-q">Lorem ipsum dolor sit amet, consectetur adipiscing elit</div><div class="faq-toggle">−</div></div>
  <p class="abs faq-answer">Lorem ipsum dolor sit amet, consectetur adipiscing elit, sed do eiusmod tempor incididunt ut labore et dolore magna aliqua. Quis ipsum suspendisse ultrices gravida. Risus commodo viverra maecenas accumsan lacus vel facilisis. <a>Read More</a></p>
</section>

<section class="newsletter">
  <h2 class="abs sec-title" style="top:3516px">Sign Up Our Newsletter</h2>
  <div class="abs news-input">Enter Your Email</div>
  <div class="abs news-btn">SUBSCRIBE</div>
</section>

<footer>
  <span class="abs foot-nav" style="left:214px">Childcare &amp; Education</span>
  <span class="abs foot-nav" style="left:395px">ChildcareCentres</span>
  <span class="abs foot-nav" style="left:546px">Online Enrollment</span>
  <span class="abs foot-nav" style="left:699px">News &amp; Advice</span>
  <span class="abs foot-nav" style="left:836px">Careers</span>
  <span class="abs foot-nav" style="left:929px">About Us</span>
  <div class="abs rule" style="top:3740px"></div>

  <div class="abs foot-brand"><span class="dot"></span>Tiny Meadow</div>

  <div class="abs contact-icon" style="left:416px;top:3787px;background:var(--orange)"><svg width="14" height="20" viewBox="0 0 10 14"><path fill="#fff" d="M5 0a5 5 0 0 0-5 5c0 3.5 5 9 5 9s5-5.5 5-9a5 5 0 0 0-5-5zm0 7a2 2 0 1 1 0-4 2 2 0 0 1 0 4z"/></svg></div>
  <p class="abs contact" style="left:416px;top:3842px">199 b Wattle Lane ipsum<br>dolor sit amet,</p>

  <div class="abs contact-icon" style="left:671px;top:3787px;background:var(--teal)"><svg width="20" height="20" viewBox="0 0 24 24"><path fill="#fff" d="M6.6 10.8a15 15 0 0 0 6.6 6.6l2.2-2.2c.3-.3.7-.4 1-.2 1.1.4 2.3.6 3.6.6.6 0 1 .4 1 1V20c0 .6-.4 1-1 1A17 17 0 0 1 3 4c0-.6.4-1 1-1h3.5c.6 0 1 .4 1 1 0 1.3.2 2.5.6 3.6.1.3 0 .7-.2 1z"/></svg></div>
  <p class="abs contact" style="left:678px;top:3842px"><b>PHONE</b><br>+61 2 5550 1473</p>

  <div class="abs contact-icon" style="left:886px;top:3787px;background:var(--green)"><svg width="20" height="16" viewBox="0 0 20 16"><rect x="1" y="1" width="18" height="14" rx="2" fill="#fff"/><path d="M1 2l9 7 9-7" fill="none" stroke="#8fc93a" stroke-width="2"/></svg></div>
  <p class="abs contact" style="left:891px;top:3842px"><b>EMAIL</b><br>hello@tinymeadow.com.au</p>

  <div class="abs rule" style="top:3946px"></div>
  <p class="abs copyright">©Copyrights 2023 Tiny Meadow Childcare &nbsp;&nbsp;|&nbsp;&nbsp; All Rights Reserved</p>
</footer>

</body>
</html>
```